Business Card Design Project

We need a business card design for an existing company in Dallas/Fort Worth that is expanding services and re-branding. We are changing the name from Brightmoor Commercial Cleaning to Keystride Facility Services. We are expanding from only commercial cleaning to include complete commercial landscape and facility maintenance services, too.

As stated, we offer a package of services that includes landscape, janitorial and facility services, which is largely unique in the industry.

We would like a design that communicates trust/partnership with a professional, corporate image, but not necessarily using the standard white business card. We would like a design that perhaps uses darker blues or perhaps a gray background, but we are open to other ideas. We might also be interested in a double-sided design - maybe with our logo on the back, printed on a gray background?

We will probably stick with the attached logo, but if you've got another inspired idea....

Target Market(s)

Property managers, commercial real estate professionals, corporate executives

Industry/Entity Type

Landscape

Requirements
Should not have
• Not interested in old style fonts.

```html
<!DOCTYPE html>
<html lang="en">
<head>
<meta charset="utf-8">
<title>Keystride Facility Services – Business Card</title>
<link rel="stylesheet" href="https://fonts.googleapis.com/css2?family=Open+Sans:wght@400;600;700&display=swap">
<style>
  :root {
    --stage-top: #8a8c8f;
    --stage-bottom: #e4e5e6;
    --card-dark: #25282c;
    --card-mid: #33373c;
    --rule-gray: #6a6e73;
    --accent-teal: #1f9cc4;
    --accent-cyan: #2aa8cc;
    --accent-blue: #0a5fb8;
    --text-white: #ffffff;
    --text-soft: #e6e8ea;
  }
  * { margin: 0; padding: 0; box-sizing: border-box; }
  html, body { width: 1200px; height: 861px; overflow: hidden; }
  body {
    background: linear-gradient(180deg, var(--stage-top) 0%, var(--stage-bottom) 100%);
    font-family: "Open Sans", Arial, sans-serif;
    display: flex; align-items: center; justify-content: center;
  }
  .card {
    position: relative;
    width: 900px; height: 514px;
    background: linear-gradient(160deg, var(--card-mid) 0%, var(--card-dark) 70%);
    box-shadow: 0 18px 40px rgba(0,0,0,.35);
    overflow: hidden;
  }
  .card__edge {
    position: absolute; top: 0; bottom: 0; width: 64px;
    background: var(--accent-cyan);
  }
  .card__edge::after {
    content: ""; position: absolute; top: 0; bottom: 0; width: 8px;
    background: var(--accent-blue);
  }
  .card__edge--left { left: 0; }
  .card__edge--left::after { right: 0; }
  .card__edge--right { right: 0; }
  .card__edge--right::after { left: 0; }
  .card__rule {
    position: absolute; top: 86px; height: 2px; background: var(--rule-gray);
  }
  .card__rule--left { left: 100px; width: 150px; }
  .card__rule--right { left: 650px; width: 150px; }
  .brand {
    position: absolute; top: 58px; left: 268px; width: 370px;
    display: flex; align-items: center; gap: 12px;
    color: var(--text-white);
  }
  .brand__mark {
    width: 56px; height: 56px; flex: none;
    border: 3px solid var(--text-white);
  }
  .brand__name { font-weight: 600; line-height: 1; }
  .brand__name-main { display: block; font-size: 34px; letter-spacing: 1px; text-transform: uppercase; }
  .brand__name-sub { display: block; font-size: 19px; letter-spacing: 1.5px; margin-top: 2px; text-transform: uppercase; }
  .brand__tagline { display: block; font-size: 8px; letter-spacing: .2px; margin-top: 4px; white-space: nowrap; }
  .person { position: absolute; left: 158px; top: 180px; }
  .person__name {
    color: var(--accent-teal); font-size: 30px; font-weight: 700; letter-spacing: .5px; line-height: 1.1;
  }
  .person__role { color: var(--text-white); font-size: 20px; font-weight: 400; margin-top: 2px; }
  .contact {
    position: absolute; left: 158px; top: 282px;
    display: grid; grid-template-columns: 100px auto; row-gap: 1px;
    font-size: 16px; line-height: 21px;
  }
  .contact dt { color: var(--accent-teal); }
  .contact dd { color: var(--text-soft); }
</style>
</head>
<body>
  <article class="card">
    <div class="card__edge card__edge--left"></div>
    <div class="card__edge card__edge--right"></div>

    <div class="card__rule card__rule--left"></div>
    <div class="card__rule card__rule--right"></div>

    <header class="brand">
      <span class="brand__mark"></span>
      <span class="brand__name">
        <span class="brand__name-main">Keystride</span>
        <span class="brand__name-sub">Facility Services</span>
        <span class="brand__tagline">Grounds, Cleaning and Building Care Under One Dependable Roof</span>
      </span>
    </header>

    <section class="person">
      <h1 class="person__name">NAME SURNAME</h1>
      <p class="person__role">Position</p>
    </section>

    <dl class="contact">
      <dt>Address</dt><dd>123 Lorem Ipsum St.. Dolor Sit City AA 1234</dd>
      <dt>Phone</dt><dd>123.456.7890</dd>
      <dt>Mobile</dt><dd>098.765.4321</dd>
      <dt>E-mail</dt><dd>name@keystridefs.com</dd>
      <dt>Facebook</dt><dd>keystridefacilityservices</dd>
      <dt>Skype</dt><dd>keystridefs</dd>
      <dt>Website</dt><dd>www.keystridefs.com</dd>
    </dl>
  </article>
</body>
</html>
```